Retail brand for customisable denim jackets

Need an interactive website where people can select sizing and colour, as well as a customisable option to add selected patches and/or pins from the inventory to be able to be drag and dropped on various locations on the denim jacket.
Base jackets also available to be bought.

Include online payment options with security.
Contact us button / feedback button

Target Market(s)

Teenagers and young adults but could include adults or others.
Currently not targeted at children.

Industry/Entity Type

Clothing Brand

Coding

Coded - Design and coding required

Number of Pages Required

3 page

Requirements
Must have
• Drag and drop of patches and pins from inventory.

A panel laying out how to order Eg 1) Pick your jacket 2) Choose your patches and pins. 3) Check out your master creation!

Colours: Light Blue, Dark Blue, Black
2d model style with the different faces of the jacket, Eg front view, back view, sleeves, shoulders etc. (for patch and pin placement)
Nice to have
• 3d cgi model of denim jacket for customer to see what their product would look like.

```html
<!DOCTYPE html>
<html lang="en">
<head>
<meta charset="utf-8">
<title>Bluethread — Customizing Denim Jackets</title>
<link rel="stylesheet" href="https://fonts.googleapis.com/css2?family=IBM+Plex+Sans:wght@500;600;700&family=Roboto:wght@400;500;700&display=swap">
<style>
:root{
  --ink:#111111;
  --black:#000000;
  --white:#ffffff;
  --soft:#f3f0f0;
  --panel:#f5f3f3;
  --line:#d9d6d6;
  --rule:#a8a8a8;
  --gold:#b58e3a;
  --text:#222222;
  --muted:#444444;
  --denim-dark:#24395a;
  --denim:#3d6596;
  --denim-light:#7f9fc4;
  --concrete:#8f9293;
}
*{box-sizing:border-box;margin:0;padding:0}
html,body{width:1200px;height:4370px;overflow:hidden}
body{position:relative;background:var(--white);font-family:"Roboto",sans-serif;color:var(--text)}
.abs{position:absolute}
.heading{font-family:"IBM Plex Sans",sans-serif;font-weight:700;letter-spacing:1px;color:var(--ink)}
.section-title{position:absolute;left:0;width:1200px;text-align:center;font-size:26px}
.title-rule{position:absolute;left:575px;width:50px;height:3px;background:var(--rule)}

/* header */
.site-header{position:absolute;left:0;top:0;width:1200px;height:75px;background:var(--white)}
.brand-badge{position:absolute;left:132px;top:20px;width:126px;height:126px;border-radius:50%;background:var(--white);border:3px solid var(--ink);display:flex;align-items:center;justify-content:center;z-index:3}
.brand-name{font-family:"IBM Plex Sans",sans-serif;font-weight:700;font-size:16px;letter-spacing:1px;color:var(--ink)}
.main-nav a{position:absolute;top:30px;font-family:"IBM Plex Sans",sans-serif;font-weight:600;font-size:12px;color:var(--ink);text-decoration:none;letter-spacing:.3px}
.main-nav a.active{color:var(--gold);border-bottom:1px solid var(--gold);padding-bottom:2px}
.cart-count{position:absolute;left:1052px;top:22px;width:16px;height:16px;border-radius:50%;background:var(--gold);color:var(--white);font-size:10px;font-weight:700;text-align:center;line-height:16px}

/* hero */
.hero{position:absolute;left:0;top:75px;width:1200px;height:604px;background:linear-gradient(100deg,#6e7172 0%,#9a9d9e 40%,#7d8082 65%,#3e4f6a 80%,#5c6f8b 100%)}
.hero-title{position:absolute;left:160px;top:200px;font-family:"IBM Plex Sans",sans-serif;font-weight:700;font-size:50px;line-height:61px;color:var(--white);letter-spacing:2px}
.hero-btn{position:absolute;top:351px;height:43px;background:var(--white);font-family:"IBM Plex Sans",sans-serif;font-weight:700;font-size:17px;color:var(--ink);display:flex;align-items:center;justify-content:center;letter-spacing:.5px}
.hero-arrow{position:absolute;top:288px;width:34px;height:32px;background:#2b2b2b;display:flex;align-items:center;justify-content:center}

/* steps */
.step-photo{position:absolute;top:828px;width:291px;height:285px}
.step-num{position:absolute;top:1139px;width:34px;height:34px;border-radius:50%;background:var(--black);color:var(--white);font-size:20px;text-align:center;line-height:34px}
.step-title{position:absolute;top:1138px;font-family:"IBM Plex Sans",sans-serif;font-weight:700;font-size:15px;color:var(--ink)}
.step-text{position:absolute;top:1160px;font-size:13.5px;color:var(--text)}

/* jackets */
.jackets{position:absolute;left:0;top:1252px;width:1200px;height:981px;background:var(--soft)}
.dropdown{position:absolute;height:32px;background:var(--black);color:var(--white);font-family:"IBM Plex Sans",sans-serif;font-weight:600;font-size:11px;display:flex;align-items:center;justify-content:space-between;padding:0 14px 0 16px;letter-spacing:.5px}
.dropdown::after{content:"";border-left:4px solid transparent;border-right:4px solid transparent;border-top:5px solid var(--white)}
.product-photo{position:absolute;width:224px;height:294px}
.product-name{position:absolute;font-size:15px;color:var(--text)}
.product-price{position:absolute;font-size:14px;font-weight:500;color:var(--ink)}

/* patches */
.patch-box{position:absolute;left:132px;top:2391px;width:935px;height:645px;border:1px solid var(--line);background:var(--white)}
.patch-grid-bg{position:absolute;left:366px;top:2391px;width:701px;height:645px;background:var(--panel);border:1px solid var(--line)}
.category{position:absolute;left:132px;width:234px;height:52px;padding-left:20px;display:flex;align-items:center;font-family:"IBM Plex Sans",sans-serif;font-weight:500;font-size:15px;color:var(--ink);letter-spacing:.3px}
.category.current{background:var(--panel);border-top:1px solid var(--line);border-bottom:1px solid var(--line)}
.patch-tile{position:absolute;width:146px;height:142px}
.btn-add,.btn-drop{position:absolute;width:68px;height:20px;font-family:"IBM Plex Sans",sans-serif;font-weight:700;font-size:9.5px;display:flex;align-items:center;justify-content:center;letter-spacing:.3px}
.btn-add{background:var(--black);color:var(--white)}
.btn-drop{background:var(--white);color:var(--ink);border:1.5px solid var(--ink)}

/* customizer */
.customizer{position:absolute;left:0;top:3092px;width:1200px;height:601px;background:var(--soft)}
.preview-frame{position:absolute;left:132px;top:3262px;width:525px;height:366px;background:var(--white);border:1px solid var(--line)}
.preview-jacket{position:absolute;left:40px;top:45px;width:445px;height:260px;border-radius:6px;background:linear-gradient(90deg,#3a628f,#5a83b3 50%,#3a628f)}
.option-title{position:absolute;left:689px;top:3262px;font-family:"IBM Plex Sans",sans-serif;font-weight:700;font-size:14px;color:var(--ink);letter-spacing:.5px}
.option-text{position:absolute;left:689px;top:3299px;width:370px;font-size:13px;line-height:19px;color:var(--muted)}
.thumb{position:absolute;top:3427px;width:86px;height:78px;background:var(--white);border:1px solid var(--line);display:flex;align-items:center;justify-content:center}
.thumb span{display:block;width:56px;height:48px;border-radius:4px}
.select{position:absolute;top:3523px;width:177px;height:34px;border:1.5px solid #888;background:var(--white);font-family:"IBM Plex Sans",sans-serif;font-weight:600;font-size:11px;color:var(--ink);display:flex;align-items:center;justify-content:space-between;padding:0 14px}
.select::after{content:"";border-left:4px solid transparent;border-right:4px solid transparent;border-top:5px solid var(--ink)}
.add-to-cart{position:absolute;left:691px;top:3579px;width:365px;height:49px;background:var(--black);color:var(--white);font-family:"IBM Plex Sans",sans-serif;font-weight:700;font-size:17px;display:flex;align-items:center;justify-content:center;letter-spacing:.8px}

/* newsletter */
.newsletter{position:absolute;left:132px;top:3761px;width:937px;height:154px;background:#1a1a1a}
.newsletter-title{position:absolute;left:55px;top:40px;font-family:"IBM Plex Sans",sans-serif;font-weight:700;font-size:27px;line-height:37px;color:var(--white);letter-spacing:1px}
.email-field{position:absolute;left:284px;top:45px;width:587px;height:60px;border:1.5px solid #8a8a8a;color:var(--white);font-size:15px;padding-left:25px;display:flex;align-items:center}
.subscribe{position:absolute;left:739px;top:57px;width:125px;height:38px;background:var(--white);color:var(--ink);font-family:"IBM Plex Sans",sans-serif;font-weight:700;font-size:15px;display:flex;align-items:center;justify-content:center}

/* footer */
.site-footer{position:absolute;left:0;top:3978px;width:1200px;height:392px;background:var(--black);color:var(--white)}
.footer-badge{position:absolute;left:132px;top:54px;width:190px;height:192px;border-radius:50%;border:3px solid var(--white);display:flex;align-items:center;justify-content:center}
.footer-badge .brand-name{color:var(--white);font-size:22px}
.footer-head{position:absolute;top:54px;font-family:"IBM Plex Sans",sans-serif;font-weight:700;font-size:13.5px;letter-spacing:.6px}
.footer-menu{position:absolute;left:421px;top:97px;list-style:none;font-size:12.5px;line-height:21.7px;letter-spacing:.3px}
.footer-icon{position:absolute;width:26px;height:26px;border-radius:50%;background:var(--white);display:flex;align-items:center;justify-content:center}
.footer-line{position:absolute;font-size:12.5px;line-height:17px;color:#e6e6e6}
.copyright{position:absolute;left:131px;top:338px;font-size:10.5px;color:#cfcfcf}
.pay-card{position:absolute;top:334px;width:44px;height:26px;border-radius:3px}
</style>
</head>
<body>

<header class="site-header">
  <div class="brand-badge"><span class="brand-name">BLUETHREAD</span></div>
  <nav class="main-nav">
    <a class="active" style="left:460px">HOME</a>
    <a style="left:521px">ABOUT US</a>
    <a style="left:613px">SHOP</a>
    <a style="left:677px">CUSTOMIZE</a>
    <a style="left:779px">PATCH SHOP</a>
    <a style="left:888px">CONTACT US</a>
  </nav>
  <svg class="abs" style="left:997px;top:28px" width="20" height="20" viewBox="0 0 20 20"><circle cx="8" cy="8" r="6" fill="none" stroke="#111" stroke-width="2.4"/><line x1="12.5" y1="12.5" x2="18" y2="18" stroke="#111" stroke-width="2.8" stroke-linecap="round"/></svg>
  <svg class="abs" style="left:1030px;top:27px" width="28" height="24" viewBox="0 0 28 24"><path d="M1 2h4l4 13h13l3-9H7" fill="none" stroke="#111" stroke-width="2"/><circle cx="11" cy="20" r="2" fill="#111"/><circle cx="20" cy="20" r="2" fill="#111"/></svg>
  <div class="cart-count">0</div>
</header>

<section class="hero" role="img" aria-label="Photo of a man and a woman wearing denim jackets against a concrete wall">
  <h1 class="hero-title">CUSTOMIZING<br>DENIM JACKETS</h1>
  <div class="hero-btn" style="left:165px;width:135px">FEEDBACK</div>
  <div class="hero-btn" style="left:321px;width:136px">CONTACT US</div>
  <div class="hero-arrow" style="left:0"><svg width="10" height="14" viewBox="0 0 10 14"><path d="M8 1 2 7l6 6" fill="none" stroke="#fff" stroke-width="2"/></svg></div>
  <div class="hero-arrow" style="left:1166px"><svg width="10" height="14" viewBox="0 0 10 14"><path d="M2 1l6 6-6 6" fill="none" stroke="#fff" stroke-width="2"/></svg></div>
</section>

<h2 class="heading section-title" style="top:728px">CUSTOMIZATION</h2>
<div class="title-rule" style="top:777px"></div>

<div class="step-photo" style="left:132px;background:linear-gradient(160deg,#9bb07a,#4d6b3a 55%,#2f4f7a)" role="img" aria-label="Woman in a denim jacket in a green field"></div>
<div class="step-photo" style="left:455px;background:linear-gradient(180deg,#7f95ad,#3a5a80 50%,#5b4a3e)" role="img" aria-label="Man seen from the back wearing a patched denim jacket by a lake"></div>
<div class="step-photo" style="left:777px;background:linear-gradient(160deg,#8a8580,#7a9ac0 50%,#c8c2b8)" role="img" aria-label="Man in a light denim jacket with a patch"></div>

<div class="step-num" style="left:132px">1</div>
<div class="step-title" style="left:182px">PICK YOUR PIECE</div>
<div class="step-text" style="left:182px">Lorem Ipsum is simply dummy</div>
<div class="step-num" style="left:455px">2</div>
<div class="step-title" style="left:504px">PERSONALIZE</div>
<div class="step-text" style="left:504px">Lorem Ipsum is simply dummy</div>
<div class="step-num" style="left:777px">3</div>
<div class="step-title" style="left:827px">PATCHES</div>
<div class="step-text" style="left:827px">Lorem Ipsum is simply dummy</div>

<section class="jackets">
  <h2 class="heading section-title" style="top:52px">DENIM JACKETS</h2>
  <div class="dropdown" style="left:499px;top:111px;width:93px">SIZING</div>
  <div class="dropdown" style="left:607px;top:111px;width:94px">COLOUR</div>

  <div class="product-photo" style="left:132px;top:185px;background:linear-gradient(170deg,#8c9092,#3e5a80)" role="img" aria-label="Man in a denim jacket"></div>
  <div class="product-photo" style="left:373px;top:185px;background:linear-gradient(170deg,#c9b28e,#4a7fae)" role="img" aria-label="Woman in a distressed denim jacket"></div>
  <div class="product-photo" style="left:612px;top:185px;background:linear-gradient(170deg,#6b5a4a,#5d86b6)" role="img" aria-label="Man in a hat and denim jacket"></div>
  <div class="product-photo" style="left:845px;top:185px;background:linear-gradient(170deg,#9aa0a6,#2f5689 60%,#1c1c1c)" role="img" aria-label="Man in a denim jacket beside a car"></div>
  <div class="product-name" style="left:132px;top:499px">Lorem Ipsum is simply</div><div class="product-price" style="left:132px;top:522px">$248.00</div>
  <div class="product-name" style="left:373px;top:499px">Lorem Ipsum is simply</div><div class="product-price" style="left:373px;top:522px">$248.00</div>
  <div class="product-name" style="left:609px;top:499px">Lorem Ipsum is simply</div><div class="product-price" style="left:609px;top:522px">$248.00</div>
  <div class="product-name" style="left:845px;top:499px">Lorem Ipsum is simply</div><div class="product-price" style="left:845px;top:522px">$248.00</div>

  <div class="product-photo" style="left:132px;top:577px;background:linear-gradient(170deg,#b9bcb0,#27344e)" role="img" aria-label="Man in sunglasses and a dark denim jacket"></div>
  <div class="product-photo" style="left:373px;top:577px;background:linear-gradient(170deg,#a9b3bb,#2c4468 60%,#d7b9c8)" role="img" aria-label="Woman in a dark denim jacket"></div>
  <div class="product-photo" style="left:609px;top:577px;background:linear-gradient(170deg,#6d6e70,#5477a3)" role="img" aria-label="Man in a light denim jacket on a street"></div>
  <div class="product-photo" style="left:845px;top:577px;background:linear-gradient(170deg,#7e6f5c,#2f5a8c)" role="img" aria-label="Man in a sherpa collar denim jacket"></div>
  <div class="product-name" style="left:132px;top:891px">Lorem Ipsum is simply</div><div class="product-price" style="left:132px;top:914px">$248.00</div>
  <div class="product-name" style="left:373px;top:891px">Lorem Ipsum is simply</div><div class="product-price" style="left:373px;top:914px">$248.00</div>
  <div class="product-name" style="left:609px;top:891px">Lorem Ipsum is simply</div><div class="product-price" style="left:609px;top:914px">$248.00</div>
  <div class="product-name" style="left:845px;top:891px">Lorem Ipsum is simply</div><div class="product-price" style="left:845px;top:914px">$248.00</div>
</section>

<h2 class="heading section-title" style="top:2290px">PATCH</h2>
<div class="title-rule" style="top:2335px"></div>

<div class="patch-box"></div>
<div class="patch-grid-bg"></div>
<nav>
  <div class="category current" style="top:2392px">STARS</div>
  <div class="category" style="top:2445px">HEARTS</div>
  <div class="category" style="top:2497px">GIRLY GIRL</div>
  <div class="category" style="top:2549px">CREATURES</div>
  <div class="category" style="top:2601px">SMILES</div>
  <div class="category" style="top:2653px">MUNCHIES</div>
  <div class="category" style="top:2705px">NATURE</div>
  <div class="category" style="top:2757px">EXPRESSIONS</div>
  <div class="category" style="top:2809px">NUMBERS &amp; LETTERS</div>
  <div class="category" style="top:2861px">ETC ETC</div>
</nav>

<div class="patch-tile" style="left:397px;top:2422px;background:linear-gradient(135deg,#3f6996,#5b83ae)" role="img" aria-label="Rhinestone star patch on denim"></div>
<div class="patch-tile" style="left:563px;top:2422px;background:linear-gradient(135deg,#46709c,#6a90b9)" role="img" aria-label="Stitched denim star patch"></div>
<div class="patch-tile" style="left:730px;top:2422px;background:linear-gradient(135deg,#2f5a95,#4a76b0)" role="img" aria-label="Lace star patch"></div>
<div class="patch-tile" style="left:896px;top:2422px;background:#0d0d0d" role="img" aria-label="Gold and blue beaded star patch"></div>
<div class="patch-tile" style="left:397px;top:2625px;background:linear-gradient(135deg,#1d2e4a,#394b66)" role="img" aria-label="Skull star badge patch"></div>
<div class="patch-tile" style="left:563px;top:2625px;background:linear-gradient(135deg,#2f4f86,#7b97c2)" role="img" aria-label="Frayed denim star patch"></div>
<div class="patch-tile" style="left:730px;top:2625px;background:linear-gradient(135deg,#45494d,#8b8479)" role="img" aria-label="Sheriff badge star patch"></div>
<div class="patch-tile" style="left:896px;top:2625px;background:linear-gradient(135deg,#2f5687,#b78660)" role="img" aria-label="Leather star patch on denim"></div>
<div class="patch-tile" style="left:397px;top:2827px;background:linear-gradient(135deg,#8a8068,#d9b94a)" role="img" aria-label="Yellow embroidered star patch"></div>
<div class="patch-tile" style="left:563px;top:2827px;background:linear-gradient(135deg,#233a6a,#3f5a8c)" role="img" aria-label="Star print fabric patch"></div>
<div class="patch-tile" style="left:730px;top:2827px;background:linear-gradient(135deg,#3f6fae,#7aa2d0)" role="img" aria-label="Metal star pin on denim"></div>
<div class="patch-tile" style="left:896px;top:2827px;background:linear-gradient(135deg,#3a6494,#5e86b3)" role="img" aria-label="Dark star patch on denim"></div>

<div class="btn-add" style="left:397px;top:2576px">ADD</div><div class="btn-drop" style="left:475px;top:2576px">DROP</div>
<div class="btn-add" style="left:563px;top:2576px">ADD</div><div class="btn-drop" style="left:641px;top:2576px">DROP</div>
<div class="btn-add" style="left:730px;top:2576px">ADD</div><div class="btn-drop" style="left:808px;top:2576px">DROP</div>
<div class="btn-add" style="left:896px;top:2576px">ADD</div><div class="btn-drop" style="left:974px;top:2576px">DROP</div>
<div class="btn-add" style="left:397px;top:2779px">ADD</div><div class="btn-drop" style="left:475px;top:2779px">DROP</div>
<div class="btn-add" style="left:563px;top:2779px">ADD</div><div class="btn-drop" style="left:641px;top:2779px">DROP</div>
<div class="btn-add" style="left:730px;top:2779px">ADD</div><div class="btn-drop" style="left:808px;top:2779px">DROP</div>
<div class="btn-add" style="left:896px;top:2779px">ADD</div><div class="btn-drop" style="left:974px;top:2779px">DROP</div>
<div class="btn-add" style="left:397px;top:2981px">ADD</div><div class="btn-drop" style="left:475px;top:2981px">DROP</div>
<div class="btn-add" style="left:563px;top:2981px">ADD</div><div class="btn-drop" style="left:641px;top:2981px">DROP</div>
<div class="btn-add" style="left:730px;top:2981px">ADD</div><div class="btn-drop" style="left:808px;top:2981px">DROP</div>
<div class="btn-add" style="left:896px;top:2981px">ADD</div><div class="btn-drop" style="left:974px;top:2981px">DROP</div>

<section class="customizer">
  <h2 class="heading section-title" style="top:63px">CUSTOMIZE YOUR DENIM</h2>
  <div class="title-rule" style="top:115px"></div>
</section>

<div class="preview-frame">
  <div class="preview-jacket" role="img" aria-label="Front and back views of a denim jacket decorated with patches"></div>
  <svg class="abs" style="left:487px;top:20px" width="20" height="20" viewBox="0 0 20 20"><circle cx="8" cy="8" r="6" fill="none" stroke="#9a9a9a" stroke-width="2"/><line x1="12.5" y1="12.5" x2="18" y2="18" stroke="#9a9a9a" stroke-width="2.4"/></svg>
</div>

<h3 class="option-title">LOREM IPSUM IS SIMPLY DUMMY TEXT OF</h3>
<p class="option-text">There are many variations of passages of Lorem Ipsum available, but the majority have suffered alteration some form, by injected humour, or randomised words.</p>
<div class="btn-add" style="left:689px;top:3389px;width:70px;height:21px">ADD</div>
<div class="btn-drop" style="left:769px;top:3389px;width:68px;height:21px">DROP</div>
<div class="thumb" style="left:691px"><span style="background:#e3b22c" role="img" aria-label="Gold star patch"></span></div>
<div class="thumb" style="left:783px"><span style="background:#c8372d" role="img" aria-label="Red guitar patch"></span></div>
<div class="thumb" style="left:876px"><span style="background:#3b6b4a" role="img" aria-label="Rock and roll roses patch"></span></div>
<div class="thumb" style="left:969px"><span style="background:#d23a3a" role="img" aria-label="Heart with banner patch"></span></div>
<div class="select" style="left:691px">SELECT SIZE</div>
<div class="select" style="left:879px">SELECT QTY</div>
<div class="add-to-cart">ADD TO CART</div>

<section class="newsletter">
  <h2 class="newsletter-title">NEWSLETTER<br>SUBSCRIBE</h2>
  <div class="email-field">E MAIL ID</div>
  <div class="subscribe">SUBSCRIBE</div>
</section>

<footer class="site-footer">
  <div class="footer-badge"><span class="brand-name">BLUETHREAD</span></div>

  <div class="footer-head" style="left:421px">MENU</div>
  <ul class="footer-menu">
    <li>HOME</li><li>ABOUT US</li><li>SHOP</li><li>CUSTOMIZE</li><li>PATCH SHOP</li><li>CONTACT US</li>
  </ul>

  <div class="footer-head" style="left:641px">CONTACT US</div>
  <div class="footer-icon" style="left:640px;top:97px"><svg width="12" height="15" viewBox="0 0 12 15"><path d="M6 14C2 9 1 7 1 5.5a5 5 0 0 1 10 0C11 7 10 9 6 14z" fill="#111"/><circle cx="6" cy="5.5" r="1.8" fill="#fff"/></svg></div>
  <div class="footer-line" style="left:675px;top:94px">48 Cobalt Lane<br>Fairhaven, TX 75099</div>
  <div class="footer-icon" style="left:640px;top:153px"><svg width="14" height="14" viewBox="0 0 14 14"><path d="M3 1l2.5 3-1.5 1.5a8 8 0 0 0 4.5 4.5L10 8.5l3 2.5-1.5 2C6 13 1 8 1 2.5z" fill="#111"/></svg></div>
  <div class="footer-line" style="left:675px;top:150px">Call Us<br>555.014.2290</div>
  <div class="footer-icon" style="left:640px;top:209px"><svg width="14" height="10" viewBox="0 0 14 10"><rect x="0.5" y="0.5" width="13" height="9" fill="#111"/><path d="M1 1l6 5 6-5" fill="none" stroke="#fff" stroke-width="1.2"/></svg></div>
  <div class="footer-line" style="left:675px;top:206px">E mail Us<br>hello@bluethread.com</div>

  <div class="footer-head" style="left:947px">FOLLOW US</div>
  <div class="footer-icon" style="left:947px;top:97px"></div>
  <div class="footer-line" style="left:985px;top:94px">Like us on<br>FRIENDWALL</div>
  <div class="footer-icon" style="left:947px;top:153px"></div>
  <div class="footer-line" style="left:985px;top:150px">Follow us on<br>CHIRPER</div>
  <div class="footer-icon" style="left:947px;top:209px"></div>
  <div class="footer-line" style="left:985px;top:206px">Follow us on<br>WORKLINK</div>

  <div class="copyright">Copyright © 2020 All Rights Reserved</div>
  <div class="pay-card" style="left:871px;background:#ffffff"></div>
  <div class="pay-card" style="left:921px;background:#e8e8e8"></div>
  <div class="pay-card" style="left:971px;background:#ffffff"></div>
  <div class="pay-card" style="left:1023px;background:#cfd8e4"></div>
</footer>

</body>
</html>
```